Elegant, professional powerpoint design for Brisval Engineering and Mining SARLU

I’ve created a new Sub contracting company for mining industry in the Democratic Republic of Congo. With Quillmoor, I’ve created a logo. I would want a professional and beautiful powerpoint design which I will use to sell my services to mining companies in DRC. The powerpoint must have pictures of mining engines such as excavators, drones, trucks, etc

```html
<!DOCTYPE html>
<html lang="en">
<head>
<meta charset="utf-8">
<title>Brisval Engineering and Mining – Presentation Slides</title>
<link href="https://fonts.googleapis.com/css2?family=Krona+One&family=PT+Sans:wght@400;700&family=Montserrat:wght@600&display=swap" rel="stylesheet">
<style>
:root{
  --blue:#2435a3;
  --blue-dark:#1a2670;
  --gold:#e3a008;
  --gold-deep:#b8760a;
  --bronze:#8a5a06;
  --amber:#c98206;
  --ink:#3d3d3d;
  --grey:#6b6b6b;
  --paper:#ffffff;
}
*{margin:0;padding:0;box-sizing:border-box}
html,body{width:1200px;height:1111px;overflow:hidden;background:#fff}
body{position:relative;font-family:"PT Sans",sans-serif;color:var(--ink)}
.slide{position:absolute;width:509px;height:286px;background:var(--paper);overflow:hidden;box-shadow:0 4px 18px rgba(0,0,0,.14)}
.abs{position:absolute}
.heading{position:absolute;left:28px;top:16px;font-family:"Krona One",sans-serif;font-size:13.5px;letter-spacing:.3px;font-weight:400;white-space:nowrap}
.heading .gold{color:var(--gold-deep)}
.heading .blue{color:var(--blue)}
.heading-rule{position:absolute;left:28px;top:36px;width:24px;height:3px;background:var(--gold-deep)}
.mark{position:absolute;right:8px;top:8px;display:flex;align-items:center;gap:3px;font-weight:700;font-size:10px;color:var(--blue)}
.mark .sq{width:9px;height:9px;background:var(--gold-deep)}
.mark.light{color:#fff}
.footer{position:absolute;left:0;bottom:0;width:509px;height:18px}
.footer svg{position:absolute;left:0;top:0}
.footer span{position:absolute;top:4px;font-size:6.5px;color:#fff;display:flex;align-items:center;gap:3px;white-space:nowrap}
.photo{position:absolute}
.lead{font-weight:700;font-size:11.5px;line-height:16px;color:#444}
.body{font-size:8.3px;line-height:13.8px;color:var(--grey)}

/* title slide */
.title-slide{left:70px;top:77px;background:linear-gradient(135deg,#f8ece1 0%,#efe5dc 55%,#e4ddd6 100%)}
.title-slide .brand-sq{left:223px;top:48px;width:62px;height:62px;background:linear-gradient(180deg,var(--gold),var(--gold-deep))}
.title-slide .brand{left:0;width:509px;top:130px;text-align:center;color:var(--blue);font-weight:700;line-height:1}
.title-slide .brand .big{display:block;font-size:50px;letter-spacing:3px}
.title-slide .brand .small{display:block;font-size:18px;letter-spacing:3px;margin-top:6px}
.title-slide .band{left:0;bottom:0;width:509px;height:20px;background:var(--blue);color:#fff;font-family:"Montserrat",sans-serif;font-size:8px;text-align:center;line-height:20px;letter-spacing:.5px}

/* about */
.about-slide{left:619px;top:77px}
.about-slide .photo{left:16px;top:49px;width:199px;height:202px;background:linear-gradient(160deg,#6f7378 0%,#8a8a82 45%,#c49a22 70%,#5e5548 100%)}
.about-slide .copy{left:249px;top:50px;width:240px}
.about-slide .copy .body{margin-top:6px}

/* services */
.services-slide{left:70px;top:408px}
.services-slide .photo{left:0;top:0;width:509px;height:143px;background:linear-gradient(120deg,#7a3f10 0%,#a3611a 45%,#6e4012 100%)}
.services-slide .heading{left:0;width:509px;text-align:center;color:#fff;top:12px}
.services-slide .heading-rule{left:243px;top:33px;background:var(--gold)}
.services-slide .intro{left:18px;top:42px;width:473px;text-align:center;color:#fff}
.services-slide .intro .lead{color:#fff;font-size:11.5px;line-height:16px;width:300px;margin:0 auto}
.services-slide .intro .body{color:#fff;font-size:8.3px;line-height:13.8px;margin-top:3px;font-weight:700}
.service{position:absolute;top:117px;width:100px;text-align:center}
.service .disc{width:58px;height:58px;border-radius:50%;background:#fff;margin:0 auto;box-shadow:0 2px 6px rgba(0,0,0,.18);display:flex;align-items:center;justify-content:center}
.service .glyph{width:34px;height:26px;border-radius:4px;background:linear-gradient(180deg,#d9d9d9,#a8a8a8)}
.service h3{font-size:9.5px;color:var(--gold-deep);margin-top:10px;font-weight:700}
.service p{font-size:5.2px;line-height:9px;color:var(--grey);margin-top:4px}

/* company */
.company-slide{left:619px;top:408px}
.company-slide .copy{left:28px;top:62px;width:228px}
.company-slide .copy .body{margin-top:8px;text-align:justify;font-size:8.2px}
.bar{position:absolute;width:27px;bottom:70px}
.tip{position:absolute;width:27px;height:20px;border-radius:4px;background:#2b2b2b;color:#fff;font-size:6.5px;font-weight:700;text-align:center;line-height:20px}
.tip::after{content:"";position:absolute;left:10px;bottom:-4px;border:3.5px solid transparent;border-top-color:#2b2b2b;border-bottom:0}
.year{position:absolute;top:222px;width:27px;text-align:center;font-size:6.5px;color:var(--gold-deep);font-weight:700}

/* team */
.team-slide{left:70px;top:739px}
.member{position:absolute;top:54px;width:130px;text-align:center}
.member .photo{position:relative;width:130px;height:143px;border-radius:3px}
.member h3{font-size:11.5px;font-weight:700;color:#333;margin-top:6px;white-space:nowrap}
.member .role{font-size:9px;color:#555;margin-top:4px}
.member .sub{font-size:6px;color:#555;margin-top:4px}

/* contact */
.contact-slide{left:619px;top:739px;background:linear-gradient(140deg,#2a3470 0%,#1d2660 50%,#2f3a78 100%)}
.contact-slide .brand-sq{left:90px;top:70px;width:50px;height:50px;background:#fff}
.contact-slide .brand{left:20px;top:178px;width:210px;text-align:center;color:#fff;font-weight:700;line-height:1}
.contact-slide .brand .big{display:block;font-size:30px;letter-spacing:2px}
.contact-slide .brand .small{display:block;font-size:12px;letter-spacing:2px;margin-top:5px}
.contact-box{position:absolute;left:266px;width:186px;height:64px;border:1.3px solid rgba(255,255,255,.9);border-radius:3px;color:#fff}
.contact-box svg{position:absolute;left:16px;top:22px}
.contact-box .label{position:absolute;left:39px;top:14px;font-size:8.5px}
.contact-box .value{position:absolute;left:39px;top:27px;font-size:8.5px;font-weight:700;line-height:14px;width:145px}
.contact-slide .url{left:0;width:509px;bottom:7px;text-align:center;color:#fff;font-family:"Montserrat",sans-serif;font-size:8px;letter-spacing:.5px}
</style>
</head>
<body>

<!-- Slide 1: Title -->
<section class="slide title-slide">
  <div class="abs brand-sq"></div>
  <div class="abs brand"><span class="big">BRISVAL</span><span class="small">ENGINEERING AND MINING</span></div>
  <div class="abs band">www.brisval.com</div>
</section>

<!-- Slide 2: About -->
<section class="slide about-slide">
  <h2 class="heading"><span class="gold">ABOUT</span> <span class="blue">US</span></h2>
  <div class="heading-rule"></div>
  <div class="mark"><span class="sq"></span>BRISVAL</div>
  <div class="photo" role="img" aria-label="Photo of yellow excavators under a cloudy sky"></div>
  <div class="abs copy">
    <p class="lead">Raase rspiciatis unde omnis iste natus error sit voluptatem accusantium doloremque.</p>
    <p class="body">Siase rspiciatis unde omnis iste natus error sit voluptatem accusantium doloremque laudantium, totam rem aperiam, eaque ipsa quae ab illo inventore veritatis et quasi architecto beatae vitae dicta sunt explicabo. Nemo enim ipsam voluptatem quia voluptas sit aspernatur aut odit aut fugit, sed quia consequuntur magni dolores eos qui ratione voluptatem sequi nesciunt. Neque porro quisquam est, qui dolorem ipsum quia dolor sit amet, consectetur, adipisci velit, sed quia non numquam eius modi tempora incidunt ut labore et dolore magnam aliquam</p>
  </div>
  <div class="footer">
    <svg width="509" height="18" viewBox="0 0 509 18"><defs><linearGradient id="g2" x1="0" y1="0" x2="0" y2="1"><stop offset="0" stop-color="#f0b312"/><stop offset="1" stop-color="#b8760a"/></linearGradient></defs><rect width="509" height="18" fill="#2435a3"/><polygon points="68,0 441,0 462,18 45,18" fill="url(#g2)"/></svg>
    <span style="left:102px">◍ www.brisval.com</span>
    <span style="left:217px">✉ info@brisval.com</span>
    <span style="left:330px">✆ +1 (555) 010 4477</span>
    <span style="left:478px">Page 02</span>
  </div>
</section>

<!-- Slide 3: Services -->
<section class="slide services-slide">
  <div class="photo" role="img" aria-label="Photo of a mining haul truck at an open-pit site in warm orange tones"></div>
  <h2 class="heading">OUR SERVICES</h2>
  <div class="heading-rule"></div>
  <div class="mark light"><span class="sq" style="background:#fff"></span>BRISVAL</div>
  <div class="abs intro">
    <p class="lead">Raase rspiciatis unde omnis iste natus error sit voluptatem accusantium doloremque.</p>
    <p class="body">Siase rspiciatis unde omnis iste natus error sit voluptatem accusantium doloremque laudantium, totam rem aperiam, eaque ipsa quae abillo inventore veritatis et quasi architecto beatae vitae dicta sunt explicaboi.</p>
  </div>
  <div class="service" style="left:30px"><div class="disc"><div class="glyph" role="img" aria-label="Excavator icon"></div></div><h3>Kseoiklse Seiaweo</h3><p>Siase rspiciatis unde omnis iste natus error sit voluptatem accusantium doloremque laudantium, totam rem aperiam, eaque ipsa quae ab illo inventore veritatis.</p></div>
  <div class="service" style="left:147px"><div class="disc"><div class="glyph" role="img" aria-label="Ore grab icon"></div></div><h3>Kseoiklse Seiaweo</h3><p>Siase rspiciatis unde omnis iste natus error sit voluptatem accusantium doloremque laudantium, totam rem aperiam, eaque ipsa quae ab illo inventore veritatis.</p></div>
  <div class="service" style="left:264px"><div class="disc"><div class="glyph" role="img" aria-label="Drilling rig icon"></div></div><h3>Kseoiklse Seiaweo</h3><p>Siase rspiciatis unde omnis iste natus error sit voluptatem accusantium doloremque laudantium, totam rem aperiam, eaque ipsa quae ab illo inventore veritatis.</p></div>
  <div class="service" style="left:381px"><div class="disc"><div class="glyph" role="img" aria-label="Dump truck icon"></div></div><h3>Kseoiklse Seiaweo</h3><p>Siase rspiciatis unde omnis iste natus error sit voluptatem accusantium doloremque laudantium, totam rem aperiam, eaque ipsa quae ab illo inventore veritatis.</p></div>
  <div class="footer">
    <svg width="509" height="18" viewBox="0 0 509 18"><defs><linearGradient id="g3" x1="0" y1="0" x2="0" y2="1"><stop offset="0" stop-color="#f0b312"/><stop offset="1" stop-color="#b8760a"/></linearGradient></defs><rect width="509" height="18" fill="#2435a3"/><polygon points="68,0 441,0 462,18 45,18" fill="url(#g3)"/></svg>
    <span style="left:102px">◍ www.brisval.com</span>
    <span style="left:217px">✉ info@brisval.com</span>
    <span style="left:330px">✆ +1 (555) 010 4477</span>
    <span style="left:478px">Page 03</span>
  </div>
</section>

<!-- Slide 4: Company -->
<section class="slide company-slide">
  <h2 class="heading"><span class="gold">OUR</span> <span class="blue">COMPANY</span></h2>
  <div class="heading-rule"></div>
  <div class="mark"><span class="sq"></span>BRISVAL</div>
  <div class="abs copy">
    <p class="lead">Raase rspiciatis unde omnis iste natus error sit voluptatem accusantium doloremque.</p>
    <p class="body">Siase rspiciatis unde omnis isklste natus error sit voluptatem accusantium doloremque laudantium, totam rem aperiam, eaque ipsa quae ab illo inventore veritatis et quasi architecto beatae vitae dicta sunt explicabo. asdklfoeemo enim ipsam voluptatem quia voluptas sit aspernatur aut odit aut fugit, sed quia consequuntur magni dolores eos qui ratione voluptatem sequi nesciunt. Neque porro quisquam est, qui dolorem ipsum quia dolor sit amet, consectetur, adipisci velit, sed quia non numquam eius modi tempora incidunt ut labore et dolore magnam aliquam</p>
  </div>
  <div class="bar" style="left:294px;height:147px;background:var(--blue)"></div>
  <div class="tip" style="left:294px;top:38px">105</div>
  <div class="year" style="left:294px">2009</div>
  <div class="bar" style="left:338px;height:62px;background:var(--gold)"></div>
  <div class="tip" style="left:338px;top:134px">44</div>
  <div class="year" style="left:338px">2013</div>
  <div class="bar" style="left:382px;height:100px;background:var(--bronze)"></div>
  <div class="tip" style="left:382px;top:85px">71</div>
  <div class="year" style="left:382px">2017</div>
  <div class="bar" style="left:426px;height:131px;background:var(--amber)"></div>
  <div class="tip" style="left:426px;top:55px">97</div>
  <div class="year" style="left:426px">2022</div>
  <div class="footer">
    <svg width="509" height="18" viewBox="0 0 509 18"><defs><linearGradient id="g4" x1="0" y1="0" x2="0" y2="1"><stop offset="0" stop-color="#f0b312"/><stop offset="1" stop-color="#b8760a"/></linearGradient></defs><rect width="509" height="18" fill="#2435a3"/><polygon points="68,0 441,0 462,18 45,18" fill="url(#g4)"/></svg>
    <span style="left:102px">◍ www.brisval.com</span>
    <span style="left:217px">✉ info@brisval.com</span>
    <span style="left:330px">✆ +1 (555) 010 4477</span>
    <span style="left:478px">Page 04</span>
  </div>
</section>

<!-- Slide 5: Team -->
<section class="slide team-slide">
  <h2 class="heading"><span class="gold">OUR</span> <span class="blue">TEAM</span></h2>
  <div class="heading-rule"></div>
  <div class="mark"><span class="sq"></span>BRISVAL</div>
  <div class="member" style="left:29px"><div class="photo" role="img" aria-label="Portrait of an executive in a navy suit" style="background:linear-gradient(160deg,#8a6a52,#3e3a40 70%,#2a3048)"></div><h3>Daniel Moreau Okafor</h3><p class="role">Ceo, Ewaiso</p><p class="sub">SIES, OSEIIK, IEOSM</p></div>
  <div class="member" style="left:189px"><div class="photo" role="img" aria-label="Portrait of an engineer in a hard hat and safety vest" style="background:linear-gradient(160deg,#6f7a5a,#b89a40 50%,#e58a2a)"></div><h3>Daniel Moreau Okafor</h3><p class="role">Ceo, Ewaiso</p><p class="sub">SIES, OSEIIK, IEOSM</p></div>
  <div class="member" style="left:350px"><div class="photo" role="img" aria-label="Portrait of a miner in a red helmet with headlamp" style="background:linear-gradient(160deg,#8a8a8a,#5a4a48 55%,#2c2c30)"></div><h3>Daniel Moreau Okafor</h3><p class="role">Ceo, Ewaiso</p><p class="sub">SIES, OSEIIK, IEOSM</p></div>
  <div class="footer">
    <svg width="509" height="18" viewBox="0 0 509 18"><defs><linearGradient id="g5" x1="0" y1="0" x2="0" y2="1"><stop offset="0" stop-color="#f0b312"/><stop offset="1" stop-color="#b8760a"/></linearGradient></defs><rect width="509" height="18" fill="#2435a3"/><polygon points="68,0 441,0 462,18 45,18" fill="url(#g5)"/></svg>
    <span style="left:102px">◍ www.brisval.com</span>
    <span style="left:217px">✉ info@brisval.com</span>
    <span style="left:330px">✆ +1 (555) 010 4477</span>
    <span style="left:478px">Page 05</span>
  </div>
</section>

<!-- Slide 6: Contact -->
<section class="slide contact-slide" role="img" aria-label="Dark blue toned photo of a large mining loader among rocks">
  <div class="abs brand-sq"></div>
  <div class="abs brand"><span class="big">BRISVAL</span><span class="small">ENGINEERING AND MINING</span></div>
  <div class="contact-box" style="top:40px">
    <svg width="10" height="14" viewBox="0 0 10 14"><path d="M5 0a5 5 0 0 0-5 5c0 4 5 9 5 9s5-5 5-9a5 5 0 0 0-5-5zm0 7a2 2 0 1 1 0-4 2 2 0 0 1 0 4z" fill="#e3a008"/></svg>
    <p class="label">Address</p>
    <p class="value">118 Kivu Ridge Rd, Mwelani, Tshilobo, 40219</p>
  </div>
  <div class="contact-box" style="top:110px">
    <svg width="12" height="12" viewBox="0 0 12 12"><path d="M2.4 0.6 4.2 2.8c.3.4.3.9 0 1.2L3.3 5c.7 1.5 2.1 2.9 3.7 3.7l1-.9c.3-.3.8-.3 1.2 0l2.2 1.8c.4.3.4.9 0 1.3l-1 1C8.8 13 0 4.6.6 2.2l1-1.4c.2-.4.6-.4.8-.2z" fill="#e3a008"/></svg>
    <p class="label">Call Us</p>
    <p class="value">+243 (555) 014 2207</p>
  </div>
  <div class="contact-box" style="top:180px">
    <svg width="13" height="10" viewBox="0 0 13 10"><rect width="13" height="10" rx="1" fill="#e3a008"/><path d="M0.5 1 6.5 6 12.5 1" stroke="#1d2660" stroke-width="1.2" fill="none"/></svg>
    <p class="label">Email</p>
    <p class="value">info@brisval.com</p>
  </div>
  <div class="abs url">www.brisval.com</div>
</section>

</body>
</html>
```